Looking for a unique designer to design new & exciting stationery for progressive professional firm

Hello! We would like to stand out, but in a good way. We want a modern unique image, something creative, but remain professional. Also portray integrity and look approachable. We want to appeal to the younger generation while not losing the respect of our more conservative older clients!

Our focus at Harbourline Partners is on guiding our clients and assisting them to 'Steady Counsel, Clear Results'. We are a small boutique accounting firm based in Melbourne Australia.

Using our 2 distinctive colours (blue & yellow) and new logo design attached, please design a modern and professional letterhead, with compliments slip and business card for our firm.

The necessary words and logos to be included on the letterhead and card are attached, the overall design of the stationery however is up to your talent. Font to be modern, professional & progressive! I like the font style (LV docs Trebuchet MS) on my draft letterhead design attached. It looks modern, professional but approachable so something like that would be great.

For the business card, I like the attached version's REAR side of the business card but not the front side, so please come up with a design for the front that will match the letterhead design you come up with. I don't like how the company name sits tightly below the logo, they make the logo look too large in proportion to the words. Also feel free to change the rear side if you believe you have a better design :)

The colours are blue R31 G125 B165
and yellow R224 G201 B24, but please convert to CMYK equivalent.

At full sizing for the card, withcomps slip and letterhead respectively, the images need to be at least 300 dpi or higher.

Please advise if you need any other files (eg for higher resolution) or information and/or refer to our website for further input.

Thank you, with great anticipation...

Dale

Target Market(s)

Discerning (and wealthy?) clients, both business owners and personal, looking for a progressive, approachable but professional accounting firm. Need to attract and appeal to the younger generations while not losing the respect of the older more conservative generation.

Industry/Entity Type

Accounting

Font styles to use
Other font styles liked:
• Something like LV doc's Trebuchet MS - for company name. Happy for you to suggest other font for other wording.

Requirements
Must have
• My company logo, QFA logo, the wording I have included on the sample of letterhead and business card.
• The colours are blue R31 G125 B165 and yellow R224 G201 B24, but please convert to CMYK equivalent. Also use a grey for smaller wording. Refer sample letterhead attached. Note that the blue and yellow on the QFA logo are not the same as the my blue and yellow above. They will and should look different.
• Note: QFA logo must have a space around it of at least half the width of the yellow part of the logo - per my attached letter sample. The logo must be at least 15mm in width on all stationery. Also the QFA logo must have the words adjacent to it, 'Harbourline Partners Pty Ltd is a QFA practice'.
Nice to have
• Maybe curved features at bottom and/or top of letterhead instead of the rectangle coloured bars that my sample letter has.
• Good to maybe have Icons for telephone, fax email address etc.
Should not have
• No other colours except my blue, yellow and black, grey and white.
• No detailed pictures as I want to keep the design modern, minimalistic and flat.

```html
<!DOCTYPE html>
<html lang="en">
<head>
<meta charset="utf-8">
<title>Harbourline Partners Letterhead</title>
<link href="https://fonts.googleapis.com/css2?family=Montserrat:ital,wght@0,400;0,500;0,600;1,400&display=swap" rel="stylesheet">
<style>
:root{
  --blue:#3f6fa6;
  --yellow:#d3c132;
  --ink:#2b2b2b;
  --grey:#5e5e5e;
  --paper:#f8f8f7;
  --backdrop:#d8d8da;
  --rule:#c9c9c9;
  --band-grey:#e4e4e4;
}
*{margin:0;padding:0;box-sizing:border-box}
html,body{width:1200px;height:859px;overflow:hidden}
body{background:var(--backdrop);font-family:"Montserrat",sans-serif;color:var(--ink);position:relative}
.letterhead{position:absolute;top:77px;width:499px;height:705px;background:var(--paper);overflow:hidden}
.letterhead--classic{left:77px}
.letterhead--banner{left:624px}
.abs{position:absolute}
.brand{left:32px;top:38px;display:flex;align-items:flex-start;gap:7px}
.brand__dot{width:53px;height:53px;border-radius:50%;background:var(--blue);flex:none}
.brand__name{font-weight:500;font-size:14px;line-height:16px;color:var(--blue);text-transform:uppercase;letter-spacing:.3px;margin-top:6px}
.brand__tagline{font-style:italic;font-size:5.4px;line-height:7px;color:var(--grey);margin-top:2px;text-transform:none;font-weight:400;letter-spacing:0}
.badge{width:43px;height:19px;background:var(--blue);display:flex;justify-content:flex-end}
.badge__tab{width:14px;height:100%;background:var(--yellow)}
.small{font-size:5.4px;line-height:7px;color:var(--grey)}
.contacts{font-size:6.4px;line-height:9px;color:var(--grey);list-style:none}
.contacts li{display:flex;align-items:center;gap:5px}
.contacts svg{width:6px;height:6px;flex:none}
.address{font-size:6.4px;line-height:9px;color:var(--grey)}
.date,.recipient{left:32px;font-size:6.8px;line-height:9px}
.date{top:169px}
.recipient{top:187px}
.letter{left:32px;top:267px;width:436px;font-size:6.3px;line-height:8.8px;letter-spacing:-.12px}
.letter__salutation{font-weight:600;margin-bottom:9px}
.letter p{text-align:justify;margin-bottom:9px}
.signoff{left:32px;top:472px;font-size:6.8px;line-height:9px}
.signoff strong{font-weight:600}
.signature{left:98px;top:467px;width:110px;height:54px;background:linear-gradient(135deg,rgba(63,111,166,.10),rgba(63,111,166,.22));border-radius:4px}
.divider{left:344px;top:45px;width:1px;height:60px;background:var(--rule)}
.waves{left:0;bottom:0;width:499px;height:70px}
.footer-note{left:0;width:499px;bottom:13px;text-align:center;color:#fff;padding-right:150px;font-size:5px;line-height:6.4px}
</style>
</head>
<body>

<section class="letterhead letterhead--classic">
  <div class="abs brand">
    <div class="brand__dot"></div>
    <div class="brand__name">Harbourline<br>Partners<div class="brand__tagline">Steady Counsel, Clear Results</div></div>
  </div>

  <div class="abs badge" style="left:358px;top:38px" role="img" aria-label="Accreditation badge"><div class="badge__tab"></div></div>
  <p class="abs small" style="left:358px;top:64px">Harbourline Partners Pty Ltd<br>is a QFA Practice</p>

  <ul class="abs contacts" style="left:358px;top:85px">
    <li><svg viewBox="0 0 6 6"><rect width="6" height="6" rx="1" fill="var(--blue)"/><path d="M1.6 1.3h1l.3 1-.5.4a2.5 2.5 0 0 0 1 1l.4-.5 1 .3v1c-2 .2-3.4-1.2-3.2-3.2z" fill="#fff"/></svg>+61 3 9400 1180</li>
    <li><svg viewBox="0 0 6 6"><rect width="6" height="6" rx="1" fill="var(--blue)"/><rect x="1.4" y="1" width="3.2" height="1.6" fill="#fff"/><rect x="1" y="2.9" width="4" height="2" fill="#fff"/></svg>+61 3 9400 1181</li>
    <li><svg viewBox="0 0 6 6"><rect width="6" height="6" rx="1" fill="var(--blue)"/><rect x="1" y="1.7" width="4" height="2.8" fill="#fff"/><path d="M1 1.8l2 1.5 2-1.5" stroke="var(--blue)" stroke-width=".5" fill="none"/></svg>info@harbourline.net.au</li>
    <li><svg viewBox="0 0 6 6"><rect width="6" height="6" rx="1" fill="var(--blue)"/><circle cx="3" cy="3" r="1.8" fill="none" stroke="#fff" stroke-width=".5"/><path d="M1.2 3h3.6M3 1.2v3.6" stroke="#fff" stroke-width=".4"/></svg>www.harbourline.net.au</li>
  </ul>
  <p class="abs address" style="left:358px;top:125px">Suite 408, 61 Carrow Street<br>Hawthorn Victoria 3122</p>

  <p class="abs date">30.09.2016</p>
  <p class="abs recipient">Recipient’s name<br>Lindenweg 14<br>20251 Hamburg<br>Germany</p>

  <div class="abs letter">
    <p class="letter__salutation">Dear sir,</p>
    <p>Communication is a very integral part of living creatures, animals and humans. Communication may be verbal or written. Written communication however is only applicable to human beings. Can you even imagine a world without communication? Verbal communication can be through telephones, webcams or in person. Written communication is through letters, emails and mobile phone messages.</p>
    <p>In today’s world of great inventions and technology, letters have somehow become redundant. It is the time for text messages or chats. But they still can communicate a lot more than all other modes of communication. Organizations and various government departments still bank on letters as a strong medium of communication. There is no comparison in costs of sending letters as compared to costs of mobile phone messages though – letters are far cheaper. Letters now commonly known as “hard copy documents” are considered more relevant and important than email copies of text messages as proof or evidence of some sort.</p>
    <p>Letters speak volumes about a person or an organization that writes it. So one must take utmost care ensuring that the language used in any letter is appropriate for the occasion for which it is being written. Since a letter is also a written proof or document, if there are certain things that should not form a part of it, then that too should be carefully handled.</p>
    <p>Writing a good letter is an art. But if for some reason someone is unable to write that perfect letter, these different types of letters provide a base for you to build on. Sample letters have been given for everyone to understand what all information needs to form a part of the letter type and then it can be customized.</p>
  </div>

  <p class="abs signoff">Yours Sincerely,<br><strong>Nora Ellison</strong></p>
  <div class="abs signature" role="img" aria-label="Handwritten signature of Nora Ellison"></div>

  <svg class="abs waves" viewBox="0 0 499 70" preserveAspectRatio="none" aria-hidden="true">
    <path d="M0 36 C150 8 330 2 499 12 L499 70 L0 70 Z" fill="var(--yellow)"/>
    <path d="M0 44 C150 20 300 14 499 22 L499 70 L0 70 Z" fill="var(--band-grey)"/>
    <path d="M0 50 C110 30 250 20 340 24 C420 28 465 40 499 46 L499 70 L0 70 Z" fill="var(--blue)"/>
  </svg>
  <p class="abs small footer-note">Liability limited by a scheme approved under<br>Professional Standards Legislation · ABN 48 213 506 774</p>
</section>

<section class="letterhead letterhead--banner">
  <div class="abs brand">
    <div class="brand__dot"></div>
    <div class="brand__name">Harbourline<br>Partners<div class="brand__tagline">Steady Counsel, Clear Results</div></div>
  </div>

  <ul class="abs contacts" style="left:225px;top:44px">
    <li><svg viewBox="0 0 6 6"><rect width="6" height="6" rx="1" fill="var(--blue)"/><path d="M1.6 1.3h1l.3 1-.5.4a2.5 2.5 0 0 0 1 1l.4-.5 1 .3v1c-2 .2-3.4-1.2-3.2-3.2z" fill="#fff"/></svg>+61 3 9400 1180</li>
    <li><svg viewBox="0 0 6 6"><rect width="6" height="6" rx="1" fill="var(--blue)"/><rect x="1.4" y="1" width="3.2" height="1.6" fill="#fff"/><rect x="1" y="2.9" width="4" height="2" fill="#fff"/></svg>+61 3 9400 1181</li>
    <li><svg viewBox="0 0 6 6"><rect width="6" height="6" rx="1" fill="var(--blue)"/><rect x="1" y="1.7" width="4" height="2.8" fill="#fff"/><path d="M1 1.8l2 1.5 2-1.5" stroke="var(--blue)" stroke-width=".5" fill="none"/></svg>info@harbourline.net.au</li>
    <li><svg viewBox="0 0 6 6"><rect width="6" height="6" rx="1" fill="var(--blue)"/><circle cx="3" cy="3" r="1.8" fill="none" stroke="#fff" stroke-width=".5"/><path d="M1.2 3h3.6M3 1.2v3.6" stroke="#fff" stroke-width=".4"/></svg>www.harbourline.net.au</li>
  </ul>
  <p class="abs address" style="left:225px;top:86px">Suite 408, 61 Carrow Street<br>Hawthorn Victoria 3122</p>

  <div class="abs divider"></div>

  <div class="abs badge" style="left:354px;top:45px;width:38px;height:16px" role="img" aria-label="Accreditation badge"><div class="badge__tab" style="width:12px"></div></div>
  <p class="abs small" style="left:402px;top:47px;font-size:4.8px;line-height:6px">Harbourline Partners Pty Ltd<br>is a QFA Practice</p>
  <p class="abs small" style="left:354px;top:84px;font-size:5px;line-height:6.6px">Liability limited by a scheme approved<br>under Professional Standards Legislation<br>ABN 48 213 506 774</p>

  <p class="abs date">30.09.2016</p>
  <p class="abs recipient">Recipient’s name<br>Lindenweg 14<br>20251 Hamburg<br>Germany</p>

  <div class="abs letter">
    <p class="letter__salutation">Dear sir,</p>
    <p>Communication is a very integral part of living creatures, animals and humans. Communication may be verbal or written. Written communication however is only applicable to human beings. Can you even imagine a world without communication? Verbal communication can be through telephones, webcams or in person. Written communication is through letters, emails and mobile phone messages.</p>
    <p>In today’s world of great inventions and technology, letters have somehow become redundant. It is the time for text messages or chats. But they still can communicate a lot more than all other modes of communication. Organizations and various government departments still bank on letters as a strong medium of communication. There is no comparison in costs of sending letters as compared to costs of mobile phone messages though – letters are far cheaper. Letters now commonly known as “hard copy documents” are considered more relevant and important than email copies of text messages as proof or evidence of some sort.</p>
    <p>Letters speak volumes about a person or an organization that writes it. So one must take utmost care ensuring that the language used in any letter is appropriate for the occasion for which it is being written. Since a letter is also a written proof or document, if there are certain things that should not form a part of it, then that too should be carefully handled.</p>
    <p>Writing a good letter is an art. But if for some reason someone is unable to write that perfect letter, these different types of letters provide a base for you to build on. Sample letters have been given for everyone to understand what all information needs to form a part of the letter type and then it can be customized.</p>
  </div>

  <p class="abs signoff">Yours Sincerely,<br><strong>Nora Ellison</strong></p>
  <div class="abs signature" role="img" aria-label="Handwritten signature of Nora Ellison"></div>

  <svg class="abs waves" viewBox="0 0 499 70" preserveAspectRatio="none" aria-hidden="true">
    <path d="M0 56 C160 34 330 26 499 22 L499 70 L0 70 Z" fill="var(--yellow)"/>
    <path d="M0 60 C160 42 330 34 499 32 L499 70 L0 70 Z" fill="var(--band-grey)"/>
    <path d="M0 64 C120 50 260 44 360 48 C430 51 470 58 499 62 L499 70 L0 70 Z" fill="var(--blue)"/>
  </svg>
</section>

</body>
</html>
```